Welding and farication business card

Business name Tmb Welding & Fabrication

I need a business card made for my welding and fabrication business that is bold and stands out. My business is both welding repairs on machinery and anything else you can imagine as well as fabricating new products. i have used this service before and was very happy with the out come of my design logo. i think the card should remain fairly simple and classy but also be bold. I think a black card would best be suited to the talk with my logo on it. i feel the back of the card should just have my logo and the front have my logo email, website and phone number and maybe incorporate a pagebook and snapgallery simple if it can be made look good these arnt a necessity.
I have included both my logo and some business card ideas below

Target Market(s)

Farmers, heavy industry, earthmoving, trucking

Industry/Entity Type

Engineering

Contact Information for Business Card

0438517264
dane@tmbweldingandfabrication.com.au
www.tmbweldingandfabrication.com.au

Colors
33a6d7
0255a3

Requirements
Must have
• Dane Whitlock
my phone number 0438517264
my logo
Preferably a black card desgn
Nice to have
• List of what i do,
Sheds and carports
Ute trays
Stockyards
Trailers
Farm equipment
Stockcrates
Gateways and Entrances
Breakdowns
Maintenance
And lots more!

```html
<!DOCTYPE html>
<html lang="en">
<head>
<meta charset="utf-8">
<title>Tmb Welding &amp; Fabrication – Business Card</title>
<link href="https://fonts.googleapis.com/css2?family=Montserrat:wght@400;500;700&display=swap" rel="stylesheet">
<style>
  :root{
    --bg:#e6e6e4;
    --brand-blue:#0255a3;
    --brand-cyan:#33a6d7;
    --slate:#46505e;
    --paper:#f7f7f6;
    --dark-1:#3a3a3a;
    --dark-2:#222;
    --back-logo:#9a9a9a;
    --list-text:#e9e9e9;
  }
  *{box-sizing:border-box;margin:0;padding:0}
  html,body{width:1200px;height:801px;overflow:hidden;background:var(--bg);font-family:"Montserrat",Arial,sans-serif}
  .stage{position:relative;width:1200px;height:801px;display:flex;align-items:center;justify-content:center;gap:40px}
  .card{position:relative;width:525px;height:300px;border-bottom:4px solid var(--brand-blue);box-shadow:0 10px 24px rgba(0,0,0,.18);overflow:hidden}

  /* front */
  .card--front{background:var(--paper)}
  .brand{position:absolute;top:48px;left:150px;display:flex;align-items:center;gap:10px}
  .brand__dot{width:14px;height:14px;border-radius:50%;background:var(--brand-blue)}
  .brand__name{font-weight:700;font-size:22px;color:var(--brand-blue);letter-spacing:.5px;line-height:1.1;text-transform:uppercase}
  .divider{position:absolute;left:28px;right:28px;top:140px;height:1px;background:var(--slate)}
  .person{position:absolute;left:40px;top:158px}
  .person__name{font-weight:700;font-size:20px;color:var(--brand-blue);letter-spacing:.5px}
  .person__role{font-size:12px;color:var(--slate);margin-top:2px}
  .person__rule{width:200px;height:1px;background:var(--slate);margin:8px 0 10px}
  .contacts{list-style:none}
  .contacts li{display:flex;align-items:center;gap:10px;font-size:11px;color:var(--slate);margin-bottom:6px}
  .contacts svg{width:13px;height:13px;flex:none}
  .address{position:absolute;right:30px;top:200px;text-align:right;font-size:11px;color:var(--slate);line-height:1.5}

  /* back */
  .card--back{background:linear-gradient(160deg,var(--dark-1),var(--dark-2))}
  .torch-art{position:absolute;left:22px;top:28px;width:110px;height:250px;border-radius:40px 40px 12px 12px;background:radial-gradient(circle at 60% 15%,#2b6b7f 0,#2a3035 45%,#262626 100%)}
  .back-brand{position:absolute;left:70px;top:168px;width:210px;display:flex;align-items:center;gap:8px}
  .back-brand__dot{width:12px;height:12px;border-radius:50%;background:var(--back-logo);flex:none}
  .back-brand__name{font-weight:700;font-size:17px;line-height:1.15;color:var(--back-logo);text-transform:uppercase;letter-spacing:.5px}
  .services{position:absolute;left:300px;top:36px;list-style:none}
  .services li{display:flex;align-items:center;gap:8px;font-size:12.5px;color:var(--list-text);text-transform:uppercase;line-height:1.55;letter-spacing:.3px}
  .services li::before{content:"";width:7px;height:7px;border-radius:50%;background:var(--brand-cyan);flex:none}
</style>
</head>
<body>
<main class="stage">
  <section class="card card--front" aria-label="Card front">
    <div class="brand">
      <span class="brand__dot"></span>
      <span class="brand__name">Tmb Welding<br>&amp; Fabrication</span>
    </div>
    <div class="divider"></div>
    <div class="person">
      <p class="person__name">DANE WHITLOCK</p>
      <p class="person__role">Manager</p>
      <div class="person__rule"></div>
      <ul class="contacts">
        <li><svg viewBox="0 0 16 16"><path d="M4 1l3 3-1.5 2a8 8 0 0 0 4.5 4.5L12 9l3 3-2 3C7 15 1 9 1 3z" fill="var(--brand-blue)"/></svg>0438517264</li>
        <li><svg viewBox="0 0 16 16"><rect x="1" y="3" width="14" height="10" fill="none" stroke="var(--brand-blue)" stroke-width="1.5"/><path d="M1 3l7 6 7-6" fill="none" stroke="var(--brand-blue)" stroke-width="1.5"/></svg>dane@tmbweldingandfabrication.com.au</li>
        <li><svg viewBox="0 0 16 16"><circle cx="8" cy="8" r="7" fill="none" stroke="var(--brand-blue)" stroke-width="1.5"/><path d="M1 8h14M8 1c-3 4-3 10 0 14M8 1c3 4 3 10 0 14" fill="none" stroke="var(--brand-blue)" stroke-width="1.2"/></svg>www.tmbweldingandfabrication.com.au</li>
      </ul>
    </div>
    <p class="address">Your address<br>city, state, ZIP 0000</p>
  </section>

  <section class="card card--back" aria-label="Card back">
    <div class="torch-art" role="img" aria-label="Embossed welding torch with spark"></div>
    <div class="back-brand">
      <span class="back-brand__dot"></span>
      <span class="back-brand__name">Tmb Welding<br>&amp; Fabrication</span>
    </div>
    <ul class="services">
      <li>Sheds</li>
      <li>Ute trays</li>
      <li>Cattle and sheep yards</li>
      <li>Trailers</li>
      <li>Farm equipment</li>
      <li>Gateways and entrances</li>
      <li>Breakdowns</li>
      <li>Maintenance</li>
      <li>And lots more!</li>
    </ul>
  </section>
</main>
</body>
</html>
```